Company director needs a business card design

I am a semi-retired former senior finance executive who sits on a number of public and private company boards and do some consulting work. I work largely with emerging businesses but deal regularly with top end of town lawyers, bankers etc. I need a thoughtful but relatively conservative design which would also resonate with my younger client base. Some colour would be good. Information limited to name, address, office tel, mobile and email.

Industry/Entity Type

Finance

```html
<!DOCTYPE html>
<html lang="en">
<head>
<meta charset="utf-8">
<title>Business Card – Morgan</title>
<link rel="stylesheet" href="https://fonts.googleapis.com/css2?family=Open+Sans:wght@400;700&display=swap">
<style>
  :root {
    --stage: #2a2a2c;
    --card-white: #ffffff;
    --ink: #262626;
    --accent: #1ab0e8;
    --contact-text: #ffffff;
    --brush-light: #ededed;
    --brush-dark: #bdbdbd;
  }
  html, body {
    margin: 0;
    padding: 0;
    width: 1200px;
    height: 800px;
    overflow: hidden;
    background: var(--stage);
  }
  .stage {
    position: relative;
    width: 1200px;
    height: 800px;
    display: flex;
    align-items: center;
    justify-content: center;
  }
  .card {
    position: relative;
    width: 1050px;
    height: 600px;
    background: var(--card-white);
    overflow: hidden;
    font-family: "Open Sans", Arial, sans-serif;
  }
  .card-shapes {
    position: absolute;
    inset: 0;
  }
  .brush-ring {
    position: absolute;
    left: 600px;
    top: 0;
    width: 450px;
    height: 330px;
    background: radial-gradient(ellipse at 50% 45%, var(--brush-light) 0%, var(--brush-light) 45%, var(--brush-dark) 62%, var(--brush-light) 78%, var(--card-white) 100%);
  }
  .identity {
    position: absolute;
    left: 410px;
    top: 88px;
    line-height: 1;
  }
  .identity-name {
    margin: 0;
    font-size: 34px;
    font-weight: 700;
    color: var(--ink);
  }
  .identity-role {
    margin: 4px 0 0 26px;
    font-size: 26px;
    font-weight: 400;
    color: var(--accent);
  }
  .contact-list {
    position: absolute;
    left: 70px;
    top: 402px;
    margin: 0;
    padding: 0;
    list-style: none;
  }
  .contact-item {
    display: flex;
    align-items: center;
    height: 44px;
    font-size: 24px;
    color: var(--contact-text);
  }
  .contact-icon {
    width: 26px;
    height: 26px;
    margin-right: 42px;
    flex: none;
  }
</style>
</head>
<body>
<main class="stage">
  <article class="card">
    <svg class="card-shapes" viewBox="0 0 1050 600" width="1050" height="600" aria-hidden="true">
      <polygon points="0,270 263,380 0,380" fill="var(--ink)"/>
      <polygon points="0,380 263,380 790,600 0,600" fill="var(--accent)"/>
    </svg>

    <div class="brush-ring" role="img" aria-label="Large dark brush-stroke circle decoration"></div>

    <header class="identity">
      <h1 class="identity-name">Morgan</h1>
      <p class="identity-role">manager</p>
    </header>

    <ul class="contact-list">
      <li class="contact-item">
        <svg class="contact-icon" viewBox="0 0 24 24" aria-hidden="true"><path fill="#fff" d="M6.6 10.8a15.1 15.1 0 0 0 6.6 6.6l2.2-2.2c.3-.3.7-.4 1-.2 1.1.4 2.3.6 3.6.6.6 0 1 .4 1 1V20c0 .6-.4 1-1 1A17 17 0 0 1 3 4c0-.6.4-1 1-1h3.5c.6 0 1 .4 1 1 0 1.3.2 2.5.6 3.6.1.3 0 .7-.2 1z"/></svg>
        <span>4102-7731</span>
      </li>
      <li class="contact-item">
        <svg class="contact-icon" viewBox="0 0 24 24" aria-hidden="true"><rect x="6" y="2" width="12" height="20" rx="2" fill="none" stroke="#fff" stroke-width="2"/><circle cx="12" cy="18" r="1.2" fill="#fff"/></svg>
        <span>00 456 789 123</span>
      </li>
      <li class="contact-item">
        <svg class="contact-icon" viewBox="0 0 24 24" aria-hidden="true"><path fill="#fff" d="M12 2a7 7 0 0 0-7 7c0 5.2 7 13 7 13s7-7.8 7-13a7 7 0 0 0-7-7zm0 9.5A2.5 2.5 0 1 1 12 6.5a2.5 2.5 0 0 1 0 5z"/></svg>
        <span>412 Harbourview. BC</span>
      </li>
      <li class="contact-item">
        <svg class="contact-icon" viewBox="0 0 24 24" aria-hidden="true"><path fill="#fff" d="M2 5h20v14H2z"/><path d="M2 5l10 8 10-8" fill="none" stroke="var(--accent)" stroke-width="1.6"/></svg>
        <span>email-morgan412@mailbox.com</span>
      </li>
    </ul>
  </article>
</main>
</body>
</html>
```